Product Label Design

Need a product design for our Epsom salt product, needs to have a luxurious simple feel to it. The picture attached is our brand and wordage on it, the bag we think should be a stand up bag that should be offwhite/creme color. The other picture are products that we like. We updated the packaging to be a Kraft tube box, please see the attached photo for dimensions.

```html
<!DOCTYPE html>
<html lang="en">
<head>
<meta charset="utf-8">
<title>Premium Epsom Salt – Label</title>
<link rel="stylesheet" href="https://fonts.googleapis.com/css2?family=Cinzel:wght@700&family=Montserrat:wght@300;700;800&display=swap">
<style>
  :root {
    --paper: #fcfcf3;
    --forest: #2b5345;
    --gold: #7a6120;
  }
  * { margin: 0; padding: 0; box-sizing: border-box; }
  html, body {
    width: 1200px;
    height: 2166px;
    overflow: hidden;
    background: var(--paper);
  }
  .label {
    width: 1200px;
    height: 2166px;
    display: flex;
    flex-direction: column;
    align-items: center;
    justify-content: center;
    text-align: center;
  }
  .label__kicker {
    width: 620px;
    height: 140px;
    display: block;
  }
  .label__kicker text {
    font-family: "Montserrat", sans-serif;
    font-weight: 700;
    font-size: 62px;
    letter-spacing: 10px;
    fill: var(--gold);
  }
  .label__title {
    font-family: "Cinzel", serif;
    font-weight: 700;
    color: var(--forest);
    font-size: 196px;
    line-height: 0.86;
    letter-spacing: -4px;
    margin-top: 10px;
  }
  .label__title span { display: block; }
  .label__divider {
    width: 440px;
    height: 14px;
    margin-top: 80px;
    display: block;
  }
  .label__grain {
    font-family: "Montserrat", sans-serif;
    font-weight: 800;
    font-size: 46px;
    letter-spacing: 0.36em;
    margin-right: -0.36em;
    color: var(--gold);
    margin-top: 100px;
  }
  .label__ingredients {
    list-style: none;
    font-family: "Montserrat", sans-serif;
    font-weight: 300;
    font-size: 40px;
    line-height: 1.8;
    letter-spacing: -1px;
    color: var(--gold);
    margin-top: 90px;
  }
  .label__weight {
    font-family: "Montserrat", sans-serif;
    font-weight: 800;
    font-size: 38px;
    letter-spacing: -1px;
    color: var(--gold);
    margin-top: 120px;
  }
</style>
</head>
<body>
  <main class="label">
    <svg class="label__kicker" viewBox="0 0 620 140" aria-label="Premium">
      <path id="kicker-arc" d="M50,135 Q310,-5 570,135" fill="none"/>
      <text><textPath href="#kicker-arc" startOffset="50%" text-anchor="middle">PREMIUM</textPath></text>
    </svg>
    <h1 class="label__title"><span>EPSOM</span><span>SALT</span></h1>
    <svg class="label__divider" viewBox="0 0 440 14" role="img" aria-label="Thin gold divider line">
      <line x1="0" y1="7" x2="440" y2="7" stroke="var(--gold)" stroke-width="2"/>
    </svg>
    <p class="label__grain">NATURAL GRAIN</p>
    <ul class="label__ingredients">
      <li>MAGNESIUM FLAKES</li>
      <li>ARNICA</li>
      <li>EUCALYPTUS</li>
    </ul>
    <p class="label__weight">NET WT. 4 OZ (113G)</p>
  </main>
</body>
</html>
```